Veltracore Needs a Poster to Advertise a New Membership Offer

We need a Poster design for Veltracore Fitness Studio.
A first of it's kind membership, The Veltracore Fitness Studio combines the skills of our industry-leading Physiotherapists, Strength Coaches and Massage Therapists into one membership with a tailored plan to guide you through the fundamentals of Movement, Mobility and Recovery.
The concept is loosely based on the professional sports model, where every member of our team works together to produce lasting results for you. The final design should illustrate the bespoke nature of our program in a fun, supportive and professional space.
"Whether your aim is to be the best in the world, or the best in your world – it’s all the same to us."
Brand Guidelines
The poster should be on a black background and use our brand colour, lime green (hexcode #cefa08) as a highlight. Please don't overuse the highlight colour though. Generally, we opt for less bright colours and more of a 'street' look
Target Market(s)
The poster should attract predominantly female members, but should not exclude males. The target age range is 30-40 years female.
Industry/Entity Type
Health And Wellness
Font styles to use
Requirements
Must have
- Must Include
• VFS logo
• Tag line " Building Strong, Mobile, Bulletproof Humans"
• Call to action "Join us"
• Sized to 600(W)x900(H)mm
• Text: "A first of it's kind membership, The Veltracore Fitness Studio combines the skills of our industry-leading Physiotherapists, Strength Coaches and Massage Therapists into one membership with a tailored plan to guide you through the fundamentals of Movement, Mobility and Recovery."
Nice to have
- Ideal Inclusions
• Veltracore logo
• Text "Membership Now Open"
• Web address: veltracore.com.au
Should not have
- Don't Use:
• Too much of the highlight colour
• Cartoon imagery
• Images that are too staged or revealing (clothing). Image should fit our target market of everyday active people, not elite athletes or models.

```html
<!DOCTYPE html>
<html lang="en">
<head>
<meta charset="utf-8">
<title>Veltracore Fitness Studio – Membership Poster</title>
<link rel="stylesheet" href="https://fonts.googleapis.com/css2?family=Russo+One&family=Bebas+Neue&family=Barlow+Semi+Condensed:wght@400;500&family=Archivo+Black&family=Exo+2:wght@500&display=swap">
<style>
  :root {
    --page-bg: #e2e2e2;
    --poster-black: #1b1b1b;
    --poster-grey: #3a3a3a;
    --white: #ffffff;
    --lime: #cedc00;
    --ink: #151515;
  }
  * { box-sizing: border-box; margin: 0; padding: 0; }
  html, body {
    width: 1200px; height: 1200px; overflow: hidden;
    background: var(--page-bg);
  }
  .poster {
    position: absolute; left: 250px; top: 75px;
    width: 700px; height: 1050px;
    background: radial-gradient(ellipse 60% 45% at 50% 52%, var(--poster-grey) 0%, #262626 55%, var(--poster-black) 100%);
    color: var(--white);
    overflow: hidden;
  }
  .brand-name {
    position: absolute; top: 26px; left: 0; width: 100%;
    text-align: center;
    font-family: "Exo 2", sans-serif; font-weight: 500;
    font-size: 31px; letter-spacing: 0.5px;
  }
  .tagline {
    position: absolute; left: 0; width: 100%; text-align: center;
    font-family: "Russo One", sans-serif; text-transform: uppercase;
    white-space: nowrap; line-height: 1;
  }
  .tagline--main { top: 76px; font-size: 57px; }
  .tagline--sub { top: 133px; font-size: 34px; }
  .offer-badge { position: absolute; left: 176px; top: 184px; width: 350px; height: 46px; }
  .offer-badge__text {
    position: absolute; left: 178px; top: 193px; width: 340px;
    text-align: center;
    font-family: "Russo One", sans-serif; font-size: 19px; color: var(--ink);
  }
  .hero { position: absolute; left: 0; top: 0; width: 700px; height: 1050px; }
  .cta {
    position: absolute; top: 814px; left: 0; width: 100%;
    text-align: center;
    font-family: "Bebas Neue", sans-serif; font-size: 122px; line-height: 1;
    color: var(--lime);
  }
  .web-address {
    position: absolute; top: 922px; left: 0; width: 100%;
    text-align: center;
    font-family: "Bebas Neue", sans-serif; font-size: 33px; line-height: 1;
  }
  .web-address .highlight { color: var(--lime); }
  .intro {
    position: absolute; top: 970px; left: 30px; width: 640px;
    text-align: center; white-space: nowrap;
    font-family: "Barlow Semi Condensed", sans-serif; font-weight: 400;
    font-size: 13.6px; line-height: 18px;
  }
  .intro .highlight { color: var(--lime); font-weight: 500; }
  .base-strip {
    position: absolute; left: 0; bottom: 0; width: 100%; height: 8px;
    background: var(--lime);
  }
</style>
</head>
<body>
  <main class="poster">
    <div class="brand-name">veltracore</div>
    <h1 class="tagline tagline--main">Building Strong,</h1>
    <h2 class="tagline tagline--sub">Mobile, Bulletproof Humans</h2>

    <svg class="offer-badge" viewBox="0 0 350 46" aria-hidden="true">
      <polygon points="12,4 350,0 334,46 0,46" fill="var(--white)"/>
      <polygon points="20,0 348,0 334,42 8,42" fill="var(--lime)"/>
    </svg>
    <div class="offer-badge__text">Membership Now Open</div>

    <svg class="hero" viewBox="0 0 700 1050">
      <defs>
        <linearGradient id="runnersTone" x1="0" y1="0" x2="1" y2="1">
          <stop offset="0" stop-color="#7b6a5e" stop-opacity="0.45"/>
          <stop offset="1" stop-color="#8a8f99" stop-opacity="0.45"/>
        </linearGradient>
      </defs>
      <rect class="hero__top-bar" x="49" y="260" width="602" height="24" fill="var(--white)"/>
      <text class="hero__monogram" x="49" y="603" textLength="602" lengthAdjust="spacingAndGlyphs"
            font-family="Archivo Black, sans-serif" font-size="345" fill="var(--white)">VFS</text>
      <polygon class="hero__chevron" points="49,675 348,792 651,657 651,688 348,808 49,697" fill="var(--white)"/>
      <rect class="hero__photo" x="40" y="262" width="620" height="536" fill="url(#runnersTone)"
            role="img" aria-label="Photo of a woman and a man running side by side in athletic wear"/>
    </svg>

    <div class="cta">JOIN US</div>
    <div class="web-address">WWW.<span class="highlight">VELTRACORE</span>.COM.AU</div>
    <p class="intro">
      A first of it's kind membership, The Veltracore Fitness Studio combines the skills of our industry-leading<br>
      Physiotherapists, Strength Coaches and Massage Therapists into one membership with a tailored plan<br>
      to guide you through the fundamentals of <span class="highlight">Movement, Mobility and Recovery.</span>
    </p>
    <div class="base-strip"></div>
  </main>
</body>
</html>
```